We own a sheep, cattle ect all type of fencing importing business. Based in the high country of New Zealand and are after a business card and logo to start with. We are after a look that is world class that is eye catching and professional.

Hi contact informo is Kowhai Ridge Fencing Solutions Gareth and Marisa Pelham P.O Box 52 Tarnbrook 7391 New Zealand Phone Number. +64 21938462 Email: marpel@brightwool.example garethpelham@brightwool.example Web: www.kowhairidgefencing.example Am open to any colours

```html
<!DOCTYPE html>
<html lang="en">
<head>
<meta charset="utf-8">
<title>Kowhai Ridge Fencing Solutions – Business Card</title>
<link rel="stylesheet" href="https://fonts.googleapis.com/css2?family=Arimo:wght@400&display=swap">
<style>
  :root {
    --teal: #5f9e98;
    --gold: #ffcc00;
    --ink: #111111;
    --paper: #ffffff;
    --ring: #6a9f9a;
  }
  html, body {
    margin: 0;
    padding: 0;
    overflow: hidden;
    background: var(--paper);
  }
  .canvas {
    position: relative;
    width: 1200px;
    height: 1000px;
    overflow: hidden;
    background: var(--paper);
    font-family: "Arimo", Arial, sans-serif;
    color: var(--ink);
  }
  .card {
    position: absolute;
    left: 0;
    top: 0;
    width: 1200px;
    height: 352px;
  }
  .title-band {
    position: absolute;
    left: 0;
    top: 0;
    width: 1200px;
    height: 60px;
    background: var(--teal);
  }
  .title-band__text {
    position: absolute;
    left: 0;
    width: 1170px;
    top: 8px;
    text-align: center;
    font-size: 42px;
    line-height: 44px;
    letter-spacing: 2px;
    color: var(--paper);
    white-space: nowrap;
  }
  .brand {
    position: absolute;
    left: 28px;
    top: 82px;
    display: flex;
    align-items: center;
    gap: 16px;
  }
  .brand__name {
    font-size: 30px;
    line-height: 40px;
    letter-spacing: 1px;
    color: var(--ink);
    white-space: nowrap;
  }
  .brand__mark {
    flex: none;
  }
  .owners {
    position: absolute;
    right: 20px;
    top: 122px;
    text-align: center;
    white-space: nowrap;
  }
  .owners__names {
    font-size: 33px;
    line-height: 38px;
    letter-spacing: 1.5px;
  }
  .owners__role {
    font-size: 28px;
    line-height: 36px;
    letter-spacing: 1.5px;
  }
  .contact-band {
    position: absolute;
    left: 0;
    top: 196px;
    width: 1200px;
    height: 156px;
    background: var(--gold);
  }
  .contact {
    position: absolute;
    margin: 0;
    font-size: 29px;
    line-height: 30px;
    letter-spacing: 1.5px;
    white-space: nowrap;
  }
  .contact--address { left: 14px; top: 6px; }
  .contact--phone { left: 665px; top: 4px; }
  .contact--email-1 { left: 275px; top: 64px; }
  .contact--email-2 { left: 435px; top: 93px; }
  .contact--web { left: 166px; top: 122px; }

  .logo-lockup {
    position: absolute;
    left: 112px;
    top: 780px;
    display: flex;
    align-items: center;
    gap: 28px;
  }
  .logo-lockup__name {
    font-size: 68px;
    line-height: 92px;
    letter-spacing: 3px;
    color: var(--ink);
    white-space: nowrap;
  }
</style>
</head>
<body>
<main class="canvas">
  <section class="card">
    <header class="title-band">
      <div class="title-band__text">Kowhai Ridge Fencing Solutions</div>
    </header>

    <div class="brand">
      <div class="brand__name">Kowhai Ridge<br>Fencing Solutions</div>
      <svg class="brand__mark" width="48" height="48" viewBox="0 0 48 48" aria-hidden="true">
        <circle cx="24" cy="24" r="21" fill="none" stroke="var(--ring)" stroke-width="2"/>
      </svg>
    </div>

    <div class="owners">
      <div class="owners__names">Gareth and Marisa Pelham</div>
      <div class="owners__role">Chief Executive Officer</div>
    </div>

    <div class="contact-band">
      <p class="contact contact--address">P.O. Box 52 Tarnbrook 7391<br>New Zealand</p>
      <p class="contact contact--phone">Phone: +64 2193 8462</p>
      <p class="contact contact--email-1">E-mail: marpel@brightwool.example</p>
      <p class="contact contact--email-2">garethpelham@brightwool.example</p>
      <p class="contact contact--web">Website: http://kowhairidgefencing.example</p>
    </div>
  </section>

  <section class="logo-lockup">
    <div class="logo-lockup__name">Kowhai Ridge<br>Fencing Solutions</div>
    <svg width="100" height="100" viewBox="0 0 100 100" aria-hidden="true">
      <circle cx="50" cy="50" r="45" fill="none" stroke="var(--ring)" stroke-width="3"/>
    </svg>
  </section>
</main>
</body>
</html>
```